Telematics app - screen shots

I'm looking to visually present a concept about safe driving, sort of a way to begin a discussion with insurance companies and/or fleet managers. There are a variety of smartphone telematics apps that use gps and accelerometers to capture, report, and gamify the driving experience. These apps track the start & end of trips, speed compared to posted speed limits, changes in speed (aggressive braking & acceleration), cornering, distraction (phone movement/handling & usage - calls and texts). Often a driving score (safety score) is presented to the user. Trips are summarized. Rewards can be earned. Leaderboards show progress.

I founded a consulting company (Drovanta Solutions - www.vantorfleetlab.com) I want to have a set of Drovanta-branded screen images of a mobile telematics app that supports safe driving. I'm not looking to build the app. Each screen would show a unique aspect of safe driving (Distraction, Speed, Braking, Trips, Leaderboard, Rewards).

You get the idea if you google image "telematics apps" and "safe driving apps."

The final design could be either a finished-looking set of screens (https://www.bluquorideshare.com/wp-content/uploads/2017/01/BQR-Apps-2.png) or sort of a story board / infographic look (https://www.wirepostdaily.com/news-releases/darnwell-data-brings-connected-car-innovation-and-oem-capabilities-to-2018-gadget-futures-expo-gfx-300579082.html).

Target Market(s)

Insurance companies, fleets, telematics service providers.

Design could be included in a blog posted on my site - https://www.vantorfleetlab.com/blog-1/

Industry/Entity Type

Car Insurance

Colors

Designer to choose colors to be used in the design.

Requirements
Must have
• Visually appealing. Telematics is considered "distruptive" to the insurance industry. Want to highlight the various components of safety (distraction, speed, aggressive driving) and a the idea that a gamified experience can reduce accidents, improve safety.
• Drovanta Solutions branding/logo.
• Must to able to swap the Drovanta logo in order to customize a presentation for a possible future client.

```html
<!DOCTYPE html>
<html lang="en">
<head>
<meta charset="utf-8">
<title>Drovanta Solutions – Safe Driving App Screens</title>
<link href="https://fonts.googleapis.com/css2?family=Quicksand:wght@400;500;700&display=swap" rel="stylesheet">
<style>
:root{
  --bg:#237f9d;
  --white:#ffffff;
  --ink:#2b2b3a;
  --muted:#8a8a99;
  --red:#ee3f55;
  --orange:#f07a2c;
  --yellow:#f5b814;
  --blue-deep:#2a5bf0;
  --blue:#1f8ff2;
  --cyan:#19d3f5;
  --violet:#7a2bf0;
  --magenta:#c21fe0;
  --purple:#5b1fd8;
  --pill:#3d1a8f;
}
*{margin:0;padding:0;box-sizing:border-box}
html,body{width:1200px;height:1200px;overflow:hidden}
body{background:var(--bg);font-family:"Quicksand",sans-serif;color:var(--white);position:relative}

.brand-header{position:absolute;top:48px;left:0;width:1200px;text-align:center;font-size:34px;font-weight:700;line-height:1}

.screen-label{position:absolute;border:2px solid var(--white);border-radius:22px;width:200px;height:40px;display:flex;align-items:center;justify-content:center;font-weight:700;font-size:17px}

.screen{position:absolute;width:210px;height:420px;border-radius:26px;overflow:hidden;box-shadow:0 14px 30px rgba(0,0,0,.25)}
.screen--distraction{background:linear-gradient(160deg,var(--red) 0%,var(--orange) 50%,var(--yellow) 100%)}
.screen--speed{background:linear-gradient(165deg,var(--blue-deep) 0%,var(--blue) 45%,var(--cyan) 100%)}
.screen--leaderboard{background:linear-gradient(170deg,var(--magenta) 0%,var(--violet) 55%,var(--purple) 100%)}

.status{display:flex;justify-content:space-between;padding:10px 16px 0;font-size:8px;font-weight:700}
.app-brand{padding:8px 12px 0;font-size:15px;font-weight:700}

.center{text-align:center}
.score-ring{display:block;margin:6px auto 0}
.title{font-weight:700;font-size:18px;margin-top:4px}
.subtitle{font-size:9px;font-weight:700}

.card{background:var(--white);color:var(--ink);border-radius:10px;margin:10px 10px 0;padding:10px}
.stat-grid{display:grid;grid-template-columns:1fr 1fr;gap:10px 6px;align-items:center}
.icon-ring{width:40px;height:40px;border-radius:50%;border:2px solid var(--ink);display:flex;align-items:center;justify-content:center;margin:auto}
.stat .label{font-size:7px;color:var(--muted)}
.stat .value{font-size:13px;font-weight:700}

.speed-card{display:flex;align-items:center;gap:10px;margin:10px 0 0;border-radius:0}
.speed-card .value{font-size:15px;font-weight:700;white-space:nowrap}
.chart-title{font-size:7px;font-weight:700;text-align:center;margin-top:6px}
.chart{display:block;margin-top:2px}

.podium{display:flex;justify-content:space-around;align-items:flex-end;padding:8px 8px 0}
.podium-item{text-align:center;font-size:8px;font-weight:700}
.avatar{border-radius:50%;background:linear-gradient(135deg,#b98a74,#3a2a2a);border:2px solid var(--white);margin:0 auto 4px}
.avatar--lg{width:50px;height:50px}
.avatar--md{width:40px;height:40px}
.avatar--sm{width:22px;height:22px;border-width:1px;margin:0}
.points{display:inline-block;background:var(--pill);border-radius:8px;padding:2px 7px;margin-top:3px;font-size:8px}
.place{font-size:7px;margin-top:3px}
.tabs{display:flex;margin:10px 10px 4px;border:1px solid var(--white);border-radius:2px;font-size:7px;font-weight:700}
.tabs span{flex:1;text-align:center;padding:3px 0}
.tabs .active{background:var(--white);color:var(--violet)}
.rank-row{display:flex;align-items:center;gap:8px;padding:5px 10px;font-size:9px;font-weight:700}
.rank-row .pos{width:16px;font-size:8px}
.rank-row .who{flex:1}
.rank-row--me{background:rgba(60,20,150,.35)}
</style>
</head>
<body>

<header class="brand-header">Drovanta Solutions</header>

<div class="screen-label" style="left:335px;top:160px">Distraction Screen</div>
<div class="screen-label" style="left:920px;top:160px">Speed Screen</div>
<div class="screen-label" style="left:355px;top:700px">Leaderboard Screen</div>

<!-- Distraction -->
<section class="screen screen--distraction" style="left:110px;top:215px">
  <div class="status"><span>9:41</span><span>●●● ▮</span></div>
  <div class="app-brand">Drovanta</div>
  <div class="center">
    <svg class="score-ring" width="96" height="96" viewBox="0 0 96 96">
      <circle cx="48" cy="48" r="40" fill="none" stroke="#f5f5f5" stroke-width="7"/>
      <circle cx="48" cy="48" r="40" fill="none" stroke="#d8402e" stroke-width="7" stroke-dasharray="211 251" transform="rotate(-90 48 48)"/>
      <circle cx="48" cy="48" r="32" fill="#ec4e35"/>
      <text x="48" y="57" text-anchor="middle" font-family="Quicksand,sans-serif" font-weight="700" font-size="26" fill="#fff">84</text>
    </svg>
    <div class="title">Distraction</div>
    <div class="subtitle">Overall Score</div>
  </div>
  <div class="card stat-grid">
    <div class="icon-ring"><svg width="20" height="22" viewBox="0 0 20 22"><rect x="5" y="1" width="10" height="18" rx="2" fill="none" stroke="#2b2b3a" stroke-width="2"/><circle cx="10" cy="10" r="2.5" fill="#2ec27e"/></svg></div>
    <div class="stat"><div class="label">Texting</div><div class="value">4</div></div>
    <div class="stat"><div class="label">Handling</div><div class="value">2</div></div>
    <div class="stat"><div class="label">Handheld Calls</div><div class="value">2</div></div>
    <div class="stat"><div class="label">Handsfree Calls</div><div class="value">8</div></div>
    <div class="icon-ring"><svg width="22" height="22" viewBox="0 0 22 22"><path d="M3 15 Q11 5 19 15 L16 17 L14 14 Q11 12 8 14 L6 17 Z" fill="#2b2b3a"/><path d="M11 12 V6 M8 9 L11 6 L14 9" stroke="#2ec27e" stroke-width="2" fill="none"/></svg></div>
  </div>
</section>

<!-- Speed -->
<section class="screen screen--speed" style="left:880px;top:215px">
  <div class="status"><span>9:41</span><span>●●● ▮</span></div>
  <div class="app-brand">Drovanta</div>
  <div class="center">
    <svg class="score-ring" width="96" height="80" viewBox="0 0 96 80">
      <circle cx="48" cy="48" r="38" fill="none" stroke="#fff" stroke-width="8" stroke-dasharray="1.5 4" transform="rotate(150 48 48)" pathLength="300" opacity=".9"/>
      <text x="48" y="52" text-anchor="middle" font-family="Quicksand,sans-serif" font-weight="700" font-size="24" fill="#fff">90</text>
      <text x="48" y="66" text-anchor="middle" font-family="Quicksand,sans-serif" font-weight="700" font-size="9" fill="#fff">km / h</text>
    </svg>
    <div class="title">Speed</div>
    <div class="subtitle">Overall Score</div>
  </div>
  <div class="card speed-card">
    <svg width="46" height="46" viewBox="0 0 46 46"><circle cx="23" cy="23" r="20" fill="none" stroke="#2b2b3a" stroke-width="2"/><line x1="23" y1="23" x2="30" y2="9" stroke="#2b2b3a" stroke-width="2.5"/><circle cx="23" cy="23" r="3" fill="#2b2b3a"/></svg>
    <div><div class="stat"><div class="label">Speed Limit</div></div><div class="value">80 km / h</div></div>
  </div>
  <div class="chart-title">Speed / Distance Chart</div>
  <svg class="chart" width="210" height="110" viewBox="0 0 210 110">
    <defs><linearGradient id="wave-a" x1="0" y1="0" x2="1" y2="1"><stop offset="0" stop-color="#2a7bf0"/><stop offset="1" stop-color="#6a2bf0"/></linearGradient></defs>
    <path d="M18 80 C50 70 70 85 100 70 S150 40 200 30 V100 H18 Z" fill="url(#wave-a)"/>
    <g font-family="Quicksand,sans-serif" font-size="6" fill="#fff">
      <text x="4" y="14">160</text><text x="4" y="38">120</text><text x="6" y="62">80</text><text x="6" y="86">40</text>
      <text x="18" y="106">0</text><text x="46" y="106">5</text><text x="74" y="106">10</text><text x="102" y="106">15</text><text x="130" y="106">20</text><text x="158" y="106">25</text><text x="186" y="106">30</text>
    </g>
  </svg>
</section>

<!-- Leaderboard -->
<section class="screen screen--leaderboard" style="left:110px;top:755px">
  <div class="status"><span>9:41</span><span>●●● ▮</span></div>
  <div class="app-brand">Drovanta</div>
  <div class="title center">Leaderboard</div>
  <div class="podium">
    <div class="podium-item"><div class="avatar avatar--md" role="img" aria-label="Portrait photo of Caleb"></div>Caleb<br><span class="points">3,124</span><div class="place">2nd</div></div>
    <div class="podium-item"><div class="avatar avatar--lg" role="img" aria-label="Portrait photo of Lester"></div>Lester<br><span class="points">3,208</span><div class="place">1st</div></div>
    <div class="podium-item"><div class="avatar avatar--md" role="img" aria-label="Portrait photo of Brandon"></div>Brandon<br><span class="points">3,004</span><div class="place">3rd</div></div>
  </div>
  <div class="tabs"><span class="active">Ranking</span><span>Trend</span></div>
  <div class="rank-row"><span class="pos">4th</span><span class="avatar avatar--sm" role="img" aria-label="Portrait photo of Christopher"></span><span class="who">Christopher</span><span>2,980</span></div>
  <div class="rank-row"><span class="pos">5th</span><span class="avatar avatar--sm" role="img" aria-label="Portrait photo of Matthew"></span><span class="who">Matthew</span><span>2,807</span></div>
  <div class="rank-row rank-row--me"><span class="pos">6th</span><span class="avatar avatar--sm" role="img" aria-label="Portrait photo of the user"></span><span class="who">You</span><span>2,795</span></div>
  <div class="rank-row"><span class="pos">7th</span><span class="avatar avatar--sm" role="img" aria-label="Portrait photo of Mandisa"></span><span class="who">Mandisa</span><span>2,640</span></div>
  <div class="rank-row"><span class="pos">8th</span><span class="avatar avatar--sm" role="img" aria-label="Portrait photo of Robert"></span><span class="who">Robert</span><span>2,500</span></div>
</section>

<!-- Overview group: speed -->
<section class="screen screen--speed" style="left:690px;top:715px;height:380px">
  <div class="status"><span>9:41</span><span>●●● ▮</span></div>
  <div class="app-brand">Drovanta</div>
  <div class="center">
    <svg class="score-ring" width="96" height="80" viewBox="0 0 96 80">
      <circle cx="48" cy="48" r="38" fill="none" stroke="#fff" stroke-width="8" stroke-dasharray="1.5 4" transform="rotate(150 48 48)" pathLength="300" opacity=".9"/>
      <text x="48" y="52" text-anchor="middle" font-family="Quicksand,sans-serif" font-weight="700" font-size="24" fill="#fff">90</text>
      <text x="48" y="66" text-anchor="middle" font-family="Quicksand,sans-serif" font-weight="700" font-size="9" fill="#fff">km / h</text>
    </svg>
    <div class="title">Speed</div>
    <div class="subtitle">Overall Score</div>
  </div>
  <div class="card speed-card">
    <svg width="46" height="46" viewBox="0 0 46 46"><circle cx="23" cy="23" r="20" fill="none" stroke="#2b2b3a" stroke-width="2"/><line x1="23" y1="23" x2="30" y2="9" stroke="#2b2b3a" stroke-width="2.5"/><circle cx="23" cy="23" r="3" fill="#2b2b3a"/></svg>
    <div><div class="stat"><div class="label">Speed Limit</div></div><div class="value">80 km / h</div></div>
  </div>
  <div class="chart-title">Speed / Distance Chart</div>
  <svg class="chart" width="210" height="90" viewBox="0 0 210 110">
    <path d="M18 80 C50 70 70 85 100 70 S150 40 200 30 V100 H18 Z" fill="url(#wave-a)"/>
  </svg>
</section>

<!-- Overview group: distraction -->
<section class="screen screen--distraction" style="left:940px;top:715px;height:380px">
  <div class="status"><span>9:41</span><span>●●● ▮</span></div>
  <div class="app-brand">Drovanta</div>
  <div class="center">
    <svg class="score-ring" width="96" height="96" viewBox="0 0 96 96">
      <circle cx="48" cy="48" r="40" fill="none" stroke="#f5f5f5" stroke-width="7"/>
      <circle cx="48" cy="48" r="40" fill="none" stroke="#d8402e" stroke-width="7" stroke-dasharray="211 251" transform="rotate(-90 48 48)"/>
      <circle cx="48" cy="48" r="32" fill="#ec4e35"/>
      <text x="48" y="57" text-anchor="middle" font-family="Quicksand,sans-serif" font-weight="700" font-size="26" fill="#fff">84</text>
    </svg>
    <div class="title">Distraction</div>
    <div class="subtitle">Overall Score</div>
  </div>
  <div class="card stat-grid">
    <div class="icon-ring"><svg width="20" height="22" viewBox="0 0 20 22"><rect x="5" y="1" width="10" height="18" rx="2" fill="none" stroke="#2b2b3a" stroke-width="2"/><circle cx="10" cy="10" r="2.5" fill="#2ec27e"/></svg></div>
    <div class="stat"><div class="label">Texting</div><div class="value">4</div></div>
    <div class="icon-ring"><svg width="22" height="22" viewBox="0 0 22 22"><path d="M3 15 Q11 5 19 15 L16 17 L14 14 Q11 12 8 14 L6 17 Z" fill="#2b2b3a"/><path d="M11 12 V6 M8 9 L11 6 L14 9" stroke="#2ec27e" stroke-width="2" fill="none"/></svg></div>
    <div class="stat"><div class="label">Handheld Calls</div><div class="value">2</div></div>
  </div>
</section>

<!-- Overview group: leaderboard (front) -->
<section class="screen screen--leaderboard" style="left:815px;top:690px">
  <div class="status"><span>9:41</span><span>●●● ▮</span></div>
  <div class="app-brand">Drovanta</div>
  <div class="title center">Leaderboard</div>
  <div class="podium">
    <div class="podium-item"><div class="avatar avatar--md" role="img" aria-label="Portrait photo of Caleb"></div>Caleb<br><span class="points">3,124</span><div class="place">2nd</div></div>
    <div class="podium-item"><div class="avatar avatar--lg" role="img" aria-label="Portrait photo of Lester"></div>Lester<br><span class="points">3,208</span><div class="place">1st</div></div>
    <div class="podium-item"><div class="avatar avatar--md" role="img" aria-label="Portrait photo of Brandon"></div>Brandon<br><span class="points">3,004</span><div class="place">3rd</div></div>
  </div>
  <div class="tabs"><span class="active">Ranking</span><span>Trend</span></div>
  <div class="rank-row"><span class="pos">4th</span><span class="avatar avatar--sm" role="img" aria-label="Portrait photo of Christopher"></span><span class="who">Christopher</span><span>2,980</span></div>
  <div class="rank-row"><span class="pos">5th</span><span class="avatar avatar--sm" role="img" aria-label="Portrait photo of Matthew"></span><span class="who">Matthew</span><span>2,807</span></div>
  <div class="rank-row rank-row--me"><span class="pos">6th</span><span class="avatar avatar--sm" role="img" aria-label="Portrait photo of the user"></span><span class="who">You</span><span>2,795</span></div>
  <div class="rank-row"><span class="pos">7th</span><span class="avatar avatar--sm" role="img" aria-label="Portrait photo of Mandisa"></span><span class="who">Mandisa</span><span>2,640</span></div>
  <div class="rank-row"><span class="pos">8th</span><span class="avatar avatar--sm" role="img" aria-label="Portrait photo of Robert"></span><span class="who">Robert</span><span>2,500</span></div>
</section>

</body>
</html>
```